House-share and Room Rental Website (With Focus on the Bedroom Landing Page)

Looking for website design for our House-share (executive accommodation) and room rental business.

Our company name is: Quellnest could also be written as QuellNest or quellnest. Either is fine .. just looking for a nice clean catchy logo to go with the design.

EXAMPLES
These are examples of other websites in this field that are doing well. this is a kind of baseline.
https://dovelinter.example.au/
https://www.kestrib.example/
https://www.velunor.example/
https://www.trisbel.example/
https://www.pondmarrowseek.example.au/

Our business model is to rent rooms to people looking for high-quality accommodation. We fill the gap between those looking to rent rooms and those with rooms to rent. However, our model is slightly different from those already on the market as we looking to fill a massive gap in the market delivering upmarket rooms for rent.(Executive Accommodation) also in the back end will be coupled with a self management process in the back end.

We offer executive style accommodation that stands out above the rest. With special extras like fire safety.. and management processes that create happier homes. We are looking for a web design package that can help us grow and scale our business. We need a design that is captivating

Our MAIN focus is having a room landing page that stands out from the rest... The core of our business will rely on the promotion of the rooms in a share house... so the whole design relies on the BEDROOM landing page to drive results.

Target Market(s)

We have 2 markets we are aiming at ... the first market is people offering rooms to rent who want the highest rental return. The second market is people looking to rent safe, high-quality rooms, in houses that are well managed and looked after.

Industry/Entity Type

Share Economy

Logo Text

QuellNest

Number of Pages Required

5+ page

Font styles to use
Sans Serif

Colors
3276b5

Requirements
Must have
• A messaging system whereby we can create direct communication between those offering rooms and those looking for rooms.
• A call to action that says " Schedule an Inspection"
• Landing page for promoting rooms
• A home page for showing stock.
• Profile page for those selling rooms
• Profile page for those looking for rooms.
• A scheduling calendar for booking inspections
Nice to have
• Pages where new residents can lock in a room.. pay bond and rents.. and sign contracts
• Notifications
• SMS capabilities in the backend.
Should not have
• No script or handwriting fonts.

```html
<!DOCTYPE html>
<html lang="en">
<head>
<meta charset="utf-8">
<title>Quellnest – Testimonials and Footer</title>
<link href="https://fonts.googleapis.com/css2?family=Lato:wght@400;700;900&family=Roboto:wght@500;700&display=swap" rel="stylesheet">
<style>
:root{
  --blue:#1a8fe3;
  --blue-bright:#2a9df4;
  --bubble-blue:#4fb6f2;
  --ink:#222;
  --muted:#7a7a7a;
  --dark-bar:#2b2c2e;
  --footer:#232324;
  --footer-text:#bdbdbd;
  --red:#e52222;
  --chat-body:#ebebeb;
  --bubble-grey:#b8b8c4;
}
*{margin:0;padding:0;box-sizing:border-box}
html,body{width:1200px;height:1200px;overflow:hidden;background:#fff}
body{position:relative;font-family:'Lato',sans-serif;color:var(--ink)}
.abs{position:absolute}

.hero-photo{left:80px;top:0;width:460px;height:110px;background:linear-gradient(180deg,#3b3b40 0%,#8d8d92 55%,#fff 100%);-webkit-mask:radial-gradient(ellipse 60% 100% at 50% 0,#000 55%,transparent 100%);mask:radial-gradient(ellipse 60% 100% at 50% 0,#000 55%,transparent 100%)}
.contact-btn{left:620px;top:-14px;width:188px;height:40px;border-radius:20px;background:var(--blue);color:#fff;font-weight:700;font-size:12px;text-align:center;line-height:50px}

.section-title{left:0;width:1192px;top:158px;text-align:center;font-family:'Roboto',sans-serif;font-weight:700;font-size:22px;letter-spacing:-.4px;color:var(--ink)}
.section-sub{left:0;width:1196px;top:190px;text-align:center;font-size:12.5px;color:var(--muted);letter-spacing:.3px}

.testimonial{top:283px;width:240px}
.avatar{width:52px;height:52px;border-radius:50%;background:radial-gradient(circle at 50% 40%,#e7c6ad 0,#b9a48f 50%,#6f8aa6 100%)}
.quote{margin-top:20px;font-size:12px;line-height:18px;color:#333;white-space:nowrap}
.person{position:absolute;left:0;font-size:11px;font-weight:700;color:var(--blue)}
.role{position:absolute;left:0;font-size:10px;color:var(--muted);white-space:nowrap}
.mark{position:absolute;left:166px;font-family:'Roboto',sans-serif;font-weight:700;font-size:80px;color:#ececec;line-height:1}

.dots{left:1103px;top:390px}
.dots span{display:block;width:9px;height:9px;border-radius:5px;background:#9a9a9a;margin-bottom:3px}
.dots span.on{height:17px;background:var(--blue)}
.slide-edge{left:1032px;top:356px;width:16px;height:94px;background:#fafafa;border:1px solid #eee}

.gallery{left:0;top:542px;width:1200px;height:229px;display:flex}
.tile{position:relative;width:300px;height:229px}
.tile .price{position:absolute;font-size:9px;font-weight:700;color:#fff}
.tile .name{position:absolute;font-size:12px;font-weight:700;color:#fff}
.t1{background:linear-gradient(135deg,#9cbd3f 0,#d5c8b3 45%,#c6342f 80%,#6d4a3a 100%)}
.t2{background:linear-gradient(160deg,#3f9bb3 0,#8fc0c9 45%,#c9b7a0 80%,#7e6b5a 100%)}
.t3{background:linear-gradient(150deg,#6b5334 0,#b7986a 45%,#d9a85f 75%,#503a25 100%)}
.t4{background:linear-gradient(160deg,#d5dde0 0,#a7b7bd 45%,#3aa8c0 70%,#7b6a5d 100%)}
.tile-btn{position:absolute;top:100px;width:25px;height:25px;border-radius:50%;background:var(--blue-bright)}

.social-bar{left:0;top:771px;width:1200px;height:59px;background:var(--dark-bar);border-bottom:1px solid #3a3a3c}
.social-cell{position:absolute;top:0;width:110px;height:59px;border-left:1px solid #3d3e40}
.social-cell i{position:absolute;left:50px;top:25px;width:10px;height:10px;border-radius:50%;background:#dcdcdc}

.footer{left:0;top:830px;width:1200px;height:370px;background:var(--footer)}
.brand{left:180px;top:880px;font-size:26px;font-weight:700;color:var(--red)}
.about{left:170px;top:936px;width:290px;font-size:11.5px;line-height:22.4px;color:var(--footer-text)}
.footer-heading{position:absolute;font-family:'Roboto',sans-serif;font-weight:500;font-size:14px;color:#fff}
.links{font-size:11px;line-height:22.5px;color:#e0e0e0;list-style:none}

.post{left:470px;width:352px;height:76px}
.thumb{position:absolute;left:0;top:0;width:98px;height:76px}
.thumb.pink{background:linear-gradient(135deg,#f3b6cf,#e86aa3 60%,#f6d9e4)}
.thumb.warm{background:linear-gradient(135deg,#8a7a4a,#c7b27a 50%,#5a4b2c)}
.post .price{position:absolute;left:112px;top:2px;font-size:13px;font-weight:700;color:#fff}
.post .title{position:absolute;left:113px;top:30px;font-size:12px;font-weight:700;color:#fff}
.post .addr{position:absolute;left:128px;top:55px;font-size:8px;color:#aaa}
.post .stat{position:absolute;top:0;font-size:9px;color:#aaa;display:flex;gap:4px;align-items:center}
.divider{left:470px;top:1039px;width:352px;height:1px;background:#3b3b3b}
.cta{left:528px;top:1116px;width:144px;height:26px;background:#c92727;color:#fff;font-family:'Roboto',sans-serif;font-weight:700;font-size:11px;text-align:center;line-height:26px;letter-spacing:-.3px}

.chat{left:838px;top:699px;width:346px;height:510px;background:#fff;border-radius:6px 6px 0 0;overflow:hidden;box-shadow:0 0 10px rgba(0,0,0,.15)}
.chat-head{height:65px;background:var(--blue-bright);color:#fff;font-family:'Roboto',sans-serif;font-weight:700;font-size:20.5px;padding:22px 0 0 18px;position:relative}
.chat-body{position:absolute;top:65px;left:0;width:346px;height:310px;background:var(--chat-body)}
.bubble{position:absolute;padding:0 13px;height:39px;line-height:39px;font-size:14px;border-radius:3px;white-space:nowrap}
.bubble.in{background:var(--bubble-grey);color:#222}
.bubble.out{background:var(--bubble-blue);color:#fff}
.scroll-track{position:absolute;left:331px;top:10px;width:6px;height:290px;border-radius:3px;background:#fff}
.scroll-thumb{position:absolute;left:331px;top:10px;width:6px;height:194px;border-radius:3px;background:var(--blue-bright)}
.chat-input{position:absolute;left:14px;top:415px;width:319px;height:63px;border:2px solid #ddd;border-radius:4px}
.chat-input span{position:absolute;left:12px;top:22px;font-size:12px;font-style:italic;color:#777}
.send{position:absolute;right:2px;top:3px;width:45px;height:53px;background:var(--blue-bright);border:1px solid #1566b0;border-radius:3px}
</style>
</head>
<body>

<div class="abs hero-photo" role="img" aria-label="Photo of an agent in a dark jacket reaching out for a handshake"></div>
<div class="abs contact-btn">Contact With us</div>

<h2 class="abs section-title">Our Customar Says</h2>
<p class="abs section-sub">Absolutely Stunning Design and Functionality</p>

<div class="abs testimonial" style="left:192px">
  <div class="avatar" role="img" aria-label="Portrait of Tobin Marsh"></div>
  <p class="quote">“Duis autem vel eum iriure dolor in hen-<br>drerit in vulputate velit esse molestie<br>consequat, vel illum dolore eu feugiat<br>nulla.”</p>
  <div class="mark" style="top:148px">“</div>
  <div class="person" style="top:170px">Tobin Marsh</div>
  <div class="role" style="top:186px">Founder &amp; CEO , Brightlane Homes Inc</div>
</div>
<div class="abs testimonial" style="left:492px">
  <div class="avatar" role="img" aria-label="Portrait of Liora Penfield"></div>
  <p class="quote">“Duis autem vel eum iriure dolor in hen-<br>drerit in vulputate velit esse molestie<br>consequat, vel illum dolore eu feugiat<br>nulla.”</p>
  <div class="mark" style="top:153px">“</div>
  <div class="person" style="top:175px">Liora Penfield</div>
  <div class="role" style="top:191px">Company Agent , Hollowreach Lets Inc.</div>
</div>
<div class="abs testimonial" style="left:792px">
  <div class="avatar" role="img" aria-label="Portrait of Emery Castell"></div>
  <p class="quote">“Duis autem vel eum iriure dolor in hen-<br>drerit in vulputate velit esse molestie<br>consequat, vel illum dolore eu feugiat<br>nulla.”</p>
  <div class="mark" style="top:150px">“</div>
  <div class="person" style="top:173px">Emery Castell</div>
  <div class="role" style="top:189px">Marketing Corvale Pty Ltd.</div>
</div>
<div class="abs slide-edge"></div>
<div class="abs dots"><span></span><span></span><span class="on"></span></div>

<div class="abs gallery">
  <div class="tile t1" role="img" aria-label="Bright kids bedroom with green walls and orange accents">
    <div class="price" style="left:30px;top:176px">( $3,690/sq ft )</div>
    <div class="name" style="left:30px;top:192px">Developing a Strategy</div>
  </div>
  <div class="tile t2" role="img" aria-label="Blue bedroom with canopy bed and patchwork quilt">
    <div class="tile-btn" style="left:119px"></div>
    <div class="tile-btn" style="left:153px"></div>
    <div class="price" style="left:113px;top:137px">( $3,690/sq ft )</div>
    <div class="name" style="left:73px;top:154px;font-size:13px">Developing a strategy</div>
  </div>
  <div class="tile t3" role="img" aria-label="Warm master bedroom with padded headboard and lounge area">
    <div class="price" style="left:31px;top:176px">( $3,690/sq ft )</div>
    <div class="name" style="left:31px;top:192px">Developing a strategy</div>
  </div>
  <div class="tile t4" role="img" aria-label="Modern white bedroom with teal accents"></div>
</div>

<div class="abs social-bar" aria-label="Social links">
  <div class="social-cell" style="left:170px"><i></i></div>
  <div class="social-cell" style="left:280px"><i></i></div>
  <div class="social-cell" style="left:390px"><i></i></div>
  <div class="social-cell" style="left:500px"><i></i></div>
  <div class="social-cell" style="left:610px"><i></i></div>
  <div class="social-cell" style="left:719px;border-right:1px solid #3d3e40"><i></i></div>
</div>

<div class="abs footer"></div>
<div class="abs brand">Quellnest</div>
<p class="abs about">Lorem ipsum dolor sit amet, consectetuer adipiscing elit, sed diam nonummy nibh euismod tincidunt ut laoreet dolore magna aliquam erat volutpat.</p>
<h3 class="footer-heading" style="left:170px;top:1022px">More Information</h3>
<h3 class="footer-heading" style="left:469px;top:892px">Popular Posts</h3>
<ul class="abs links" style="left:170px;top:1059px"><li>Help Center</li><li>Terms of Use</li><li>Quellnest could Blog</li></ul>
<ul class="abs links" style="left:320px;top:1059px"><li>About Quellnest could</li><li>Careers</li><li>Terms of Use</li></ul>

<div class="abs post" style="top:942px">
  <div class="thumb pink" role="img" aria-label="Pink girls bedroom with canopy bed"></div>
  <div class="price">$125,799</div>
  <div class="title">Amazing Apartment Family</div>
  <svg class="abs" style="left:115px;top:54px" width="7" height="10" viewBox="0 0 7 10"><path d="M3.5 0A3.5 3.5 0 0 0 0 3.5C0 6 3.5 10 3.5 10S7 6 7 3.5A3.5 3.5 0 0 0 3.5 0z" fill="#2a9df4"/><circle cx="3.5" cy="3.5" r="1.3" fill="#232324"/></svg>
  <div class="addr">Larkmoor St, Brookhaven, NY, USA</div>
  <div class="stat" style="left:270px"><svg width="10" height="9" viewBox="0 0 10 9"><path d="M5 8.5 1 4.6A2.3 2.3 0 0 1 5 1.6a2.3 2.3 0 0 1 4 3z" fill="none" stroke="#aaa"/></svg>546</div>
  <div class="stat" style="left:322px"><svg width="10" height="9" viewBox="0 0 10 9"><ellipse cx="5" cy="4" rx="5" ry="3.6" fill="#bbb"/><path d="M2 6 1 9 4.5 7z" fill="#bbb"/></svg>119</div>
</div>
<div class="abs divider"></div>
<div class="abs post" style="top:1058px">
  <div class="thumb warm" role="img" aria-label="Classic living room with chandelier"></div>
  <div class="price">$125,799</div>
  <div class="title">Amazing Apartment Family</div>
  <svg class="abs" style="left:115px;top:54px" width="7" height="10" viewBox="0 0 7 10"><path d="M3.5 0A3.5 3.5 0 0 0 0 3.5C0 6 3.5 10 3.5 10S7 6 7 3.5A3.5 3.5 0 0 0 3.5 0z" fill="#2a9df4"/><circle cx="3.5" cy="3.5" r="1.3" fill="#232324"/></svg>
  <div class="addr">Larkmoor St, Brookhaven, NY, USA</div>
  <div class="stat" style="left:270px"><svg width="10" height="9" viewBox="0 0 10 9"><path d="M5 8.5 1 4.6A2.3 2.3 0 0 1 5 1.6a2.3 2.3 0 0 1 4 3z" fill="none" stroke="#aaa"/></svg>546</div>
  <div class="stat" style="left:322px"><svg width="10" height="9" viewBox="0 0 10 9"><ellipse cx="5" cy="4" rx="5" ry="3.6" fill="#bbb"/><path d="M2 6 1 9 4.5 7z" fill="#bbb"/></svg>119</div>
</div>
<div class="abs cta">SCHEDULE AN INSPECTION</div>

<aside class="abs chat">
  <div class="chat-head">Quellnest Could Live Chat
    <svg class="abs" style="left:275px;top:23px" width="76" height="24" viewBox="0 0 76 24"><path d="M0 22h22" stroke="#fff" stroke-width="2"/><path d="M46 2 64 20M64 2 46 20" stroke="#fff" stroke-width="2"/></svg>
  </div>
  <div class="chat-body">
    <svg class="abs" style="left:27px;top:32px" width="10" height="10" viewBox="0 0 10 10"><path d="M0 0v10h10z" fill="#b8b8c4"/></svg>
    <div class="bubble in" style="left:19px;top:42px">Hi!</div>
    <div class="bubble in" style="left:19px;top:96px">How may I help you?</div>
    <div class="bubble out" style="left:250px;top:146px">Hello!</div>
    <svg class="abs" style="left:301px;top:185px" width="10" height="10" viewBox="0 0 10 10"><path d="M0 0h10v10z" fill="#4fb6f2"/></svg>
    <div class="bubble out" style="left:119px;top:202px">I need help with the design.</div>
    <div class="scroll-track"></div>
    <div class="scroll-thumb"></div>
  </div>
  <svg class="abs" style="left:28px;top:384px" width="56" height="22" viewBox="0 0 56 22"><path d="M0 7h5l6-5v18l-6-5H0z" fill="#666"/><path d="M14 7q3 4 0 8M17 4q5 7 0 14" stroke="#666" stroke-width="1.5" fill="none"/><rect x="38" y="1" width="7" height="13" rx="3.5" fill="#666"/><path d="M35 10q0 6 6.5 6T48 10M41.5 16v5" stroke="#666" stroke-width="1.5" fill="none"/></svg>
  <div class="chat-input"><span>Type your message here...</span>
    <div class="send"><svg class="abs" style="left:8px;top:16px" width="30" height="20" viewBox="0 0 30 20"><path d="M0 0 30 10 0 20 5 10z" fill="#fff"/></svg></div>
  </div>
</aside>

</body>
</html>
```